Nebelkreis - needs a CD/Cover Design for a VA Compilation

We need a CD-Design/Cover-Artwork for our Various Artists Compilation called 'Nebelkreis', which means "Fog circle". Back then our events were based in one of Germanys best underground techno-clubs., which we also called "our temple".
The artists featured on this compilation rather performed at our events or had a massive influence on the music the djs played.
The sound is glitchy, technically detailed and a little unpredictable.

We would like to see some designs not too colourful!

Target Market(s)

complex electronic music listeners

Industry/Entity Type

Club

Font styles to use
Sans Serif

Colors
ec1f27

Requirements
Must have
• Ideally the artwork should be something otherworldly, abstract/glitchy, be an optical illusion and/or have geometric complexity.
Nice to have
• - probably black and white design fits better with us, but you can also try it with a very few colors.
- maybe something futuristic or scatchy
Should not have
• - it should definitely NOT be too colourful.
- no humans!! or animals
- in case you think to draw a temple, please use it more abstract, nothing too obviously, we dont wanna look like a hippie event!
- no musical notes
- no obvious "play" symbol / headphones or vinyl images

```html
<!DOCTYPE html>
<html lang="en">
<head>
<meta charset="utf-8">
<title>Nebelkreis – Various Artists Compilation</title>
<link rel="stylesheet" href="https://fonts.googleapis.com/css2?family=Share+Tech+Mono&family=Ubuntu:wght@700&display=swap">
<style>
  :root {
    --backdrop: #e9e9ee;
    --cover-dark: #2a2a2b;
    --photo-bright: #f2f2f2;
    --photo-light: #d4d4d4;
    --photo-mid: #9c9c9c;
    --photo-deep: #5a5a5a;
    --label-grey: #b9b9b9;
    --title-light: #dedede;
    --accent-red: #ec1f27;
  }
  html, body {
    margin: 0;
    width: 1200px;
    height: 909px;
    overflow: hidden;
    background: var(--backdrop);
  }
  .cover {
    position: absolute;
    left: 180px;
    top: 34px;
    width: 840px;
    height: 840px;
    background: var(--cover-dark);
    overflow: hidden;
    box-shadow: 0 6px 24px rgba(0,0,0,0.18);
  }
  .cover-art {
    position: absolute;
    inset: 0;
    width: 100%;
    height: 100%;
  }
  .compilation-label {
    position: absolute;
    left: 78px;
    top: 512px;
    margin: 0;
    font-family: "Share Tech Mono", monospace;
    font-size: 15px;
    line-height: 28px;
    letter-spacing: 0.28em;
    color: var(--label-grey);
    text-transform: uppercase;
  }
  .compilation-label span { display: block; }
  .release-title {
    position: absolute;
    left: 76px;
    top: 664px;
    margin: 0;
    font-family: "Ubuntu", sans-serif;
    font-weight: 700;
    font-size: 72px;
    line-height: 1;
    letter-spacing: -0.04em;
    text-transform: uppercase;
    white-space: nowrap;
  }
  .release-title .title-first { color: var(--title-light); }
  .release-title .title-second { color: var(--accent-red); }
</style>
</head>
<body>
  <main class="cover">
    <svg class="cover-art" viewBox="0 0 608 608" preserveAspectRatio="none">
      <defs>
        <radialGradient id="spiral-tone" cx="0.55" cy="0.3" r="0.8">
          <stop offset="0" stop-color="var(--photo-bright)"/>
          <stop offset="0.12" stop-color="var(--photo-light)"/>
          <stop offset="0.4" stop-color="var(--photo-mid)"/>
          <stop offset="0.65" stop-color="#b0b0b0"/>
          <stop offset="1" stop-color="var(--photo-deep)"/>
        </radialGradient>
      </defs>
      <rect class="architecture-photo" role="img"
            aria-label="Black and white photograph looking up into a swirling spiral concrete stairwell, its curving bands leading to a bright opening at the centre"
            x="0" y="0" width="608" height="460" fill="url(#spiral-tone)"/>
      <path class="dark-wave"
            d="M0,232 C35,205 70,180 100,184 C135,190 160,262 190,330 C222,400 252,428 295,432 C380,440 520,440 608,436 L608,608 L0,608 Z"
            fill="var(--cover-dark)"/>
    </svg>
    <p class="compilation-label">
      <span>Various</span>
      <span>Artists</span>
      <span>Compilation</span>
    </p>
    <h1 class="release-title"><span class="title-first">Nebel</span><span class="title-second">kreis</span></h1>
  </main>
</body>
</html>
```